Author needs cover design for health related book

I need the front cover designed for an upcoming book. I want a cover that will stand out when viewed in a thumbnail on sites such as Brellix. I'm open to the color scheme. The cover design should convey hopeful, uplifting energy, trust, and confidence. Nothing cute or frilly, please. The book is written for newly diagnosed cancer patients. The book title is: The Test Came Back, So Where Next? Subtitle: Steadily Facing Illness Through Dread, Confusion and Worry
Author: Marvina Tobbel
I'm not window shopping. I will definitely pick one of the submitted designs.
Target Market(s)
Newly diagnosed cancer patients
Industry/Entity Type
Health Care
Look and feel

```html
<!DOCTYPE html>
<html lang="en">
<head>
<meta charset="UTF-8">
<title>The Test Came Back, So Where Next? — Book Cover</title>
<link href="https://fonts.googleapis.com/css2?family=Bebas+Neue&family=Oswald:wght@500&display=swap" rel="stylesheet">
<style>
  :root {
    --cover-red: #f2402c;
    --cover-red-deep: #e8321f;
    --cover-red-light: #f7553d;
    --ink-white: #ffffff;
    --cell-violet: #6a4fc0;
    --cell-indigo: #3b2a86;
    --cell-glow: #8f6bd6;
  }
  * { margin: 0; padding: 0; box-sizing: border-box; }
  html, body {
    width: 886px;
    height: 1200px;
    overflow: hidden;
    background: var(--cover-red);
  }
  .book-cover {
    position: relative;
    width: 886px;
    height: 1200px;
    overflow: hidden;
    background: linear-gradient(160deg, var(--cover-red-light) 0%, var(--cover-red) 45%, var(--cover-red-deep) 100%);
    color: var(--ink-white);
  }
  .cover-illustration {
    position: absolute;
    left: 500px;
    top: 95px;
    width: 330px;
    height: 330px;
    border-radius: 50%;
    background: radial-gradient(circle at 45% 40%, var(--cell-glow) 0%, var(--cell-violet) 40%, var(--cell-indigo) 85%, rgba(59,42,134,0) 100%);
  }
  .title {
    position: absolute;
    left: 70px;
    top: 120px;
    font-family: "Bebas Neue", "Oswald", sans-serif;
    font-weight: 400;
    line-height: 0.9;
    text-transform: uppercase;
    white-space: nowrap;
  }
  .title-line { display: block; }
  .title-line--lead { font-size: 190px; }
  .title-line--mid { font-size: 182px; }
  .title-line--close {
    font-size: 150px;
    margin-top: 26px;
    letter-spacing: 0.01em;
  }
  .subtitle {
    position: absolute;
    left: 0;
    right: 0;
    top: 900px;
    text-align: center;
    font-family: "Oswald", sans-serif;
    font-weight: 500;
    font-size: 34px;
    line-height: 1.35;
    letter-spacing: 0.03em;
    text-transform: uppercase;
  }
  .author {
    position: absolute;
    left: 0;
    right: 0;
    top: 1045px;
    text-align: center;
    font-family: "Bebas Neue", "Oswald", sans-serif;
    font-size: 64px;
    letter-spacing: 0.55em;
    padding-left: 0.55em;
    text-transform: uppercase;
  }
</style>
</head>
<body>
  <main class="book-cover">
    <div class="cover-illustration" role="img" aria-label="Illustration of a violet cell surrounded by small particles"></div>
    <h1 class="title">
      <span class="title-line title-line--lead">The</span>
      <span class="title-line title-line--lead">Test</span>
      <span class="title-line title-line--mid">Came Back,</span>
      <span class="title-line title-line--close">So Where Next?</span>
    </h1>
    <p class="subtitle">Steadily Facing Illness Through<br>Dread, Confusion and Worry</p>
    <p class="author">Marvina Tobbel</p>
  </main>
</body>
</html>
```